Accountability Project Graphics

I want to create 10 social media graphics (new Instagram size 4:5 (1080 x 1350 pixels) focusing on our Kelmora Accountability App, using any of the 3 pictures attached. Use the attached pics only, NO RANDOM STOCK PHOTOGRAPHY. For the color scheme, use the landing page colors/fonts (attached).
You can add any of the 3 photos attached but I mainly need BOLD text that includes these headlines and sub-headlines on them.
Please NOTE for all the headlines below, also add this sub-headline on each graphic:
Stay Consistent with MB in Your Pocket!
Here are the headlines:
• Stop Starting Over Every Monday
• You don't need more willpower. You need more support
• Built for women who are tired of doing this alone
• When Motivation Fades, MB Checks In
• The Support System You've Been Missing
• Support When Motivation Disappears
• What if MB Checked in Every Day?
• The Missing Piece Isn't Another Diet
• Eat the food you love. Stay accountable every day.
• One Bad Meal Doesn't Mean You Failed
women over 40 trying to lose weight

```html
<!DOCTYPE html>
<html lang="en">
<head>
<meta charset="utf-8">
<title>Kelmora Accountability App — Social Graphics</title>
<link rel="stylesheet" href="https://fonts.googleapis.com/css2?family=Young+Serif&family=Poppins:wght@700&display=swap">
<style>
:root{
  --stage:#8c8c8e;
  --ink:#2b1a3d;
  --rose:#c9567c;
  --rose-deep:#c04f74;
  --blush:#f1b9d3;
  --card-top:#fdf3f8;
  --card-bottom:#fbd5e6;
  --photo-warm-a:#e9d2bd;
  --photo-warm-b:#5b4a4f;
  --outfit-a:#3a3550;
  --outfit-b:#1c1d2e;
}
*{margin:0;padding:0;box-sizing:border-box}
html,body{width:1200px;height:2957px;overflow:hidden;background:var(--stage)}
.board{position:relative;width:1200px;height:2957px}
.card{position:absolute;width:431px;height:538px;overflow:hidden;
  background:linear-gradient(180deg,var(--card-top) 0%,var(--card-bottom) 100%)}
.col-l{left:156px}.col-r{left:613px}
.row-1{top:79px}.row-2{top:645px}.row-3{top:1210px}.row-4{top:1775px}.row-5{top:2340px}
.shape{position:absolute;border-radius:50%}
.ring{background:var(--rose-deep)}
.soft{background:var(--blush)}
.white{background:#fff}
.photo{position:absolute;border-radius:50%;
  background:radial-gradient(circle at 55% 40%,var(--photo-warm-a) 0%,#c9a894 45%,var(--photo-warm-b) 100%)}
.cutout{position:absolute;border-radius:60px 60px 0 0;
  background:linear-gradient(180deg,#4a3a3f 0%,var(--outfit-a) 22%,var(--outfit-b) 100%)}
.headline{position:absolute;z-index:2;font-family:"Young Serif",Georgia,serif;color:var(--ink);line-height:1.02;white-space:nowrap}
.headline .accent{color:var(--rose)}
.tagline{position:absolute;z-index:2;font-family:"Poppins",Arial,sans-serif;font-weight:700;color:var(--ink);line-height:1.3;white-space:nowrap}
.tagline .accent{color:var(--rose)}
.right{text-align:right}.center{text-align:center}
</style>
</head>
<body>
<main class="board">

<section class="card col-l row-1">
  <div class="shape ring" style="left:144px;top:186px;width:620px;height:620px"></div>
  <div class="shape soft" style="left:176px;top:170px;width:620px;height:620px"></div>
  <div class="cutout" role="img" aria-label="Coach smiling in black lace top and jeans, hand on hip" style="left:272px;top:108px;width:159px;height:430px"></div>
  <h2 class="headline" style="left:27px;top:32px;font-size:52px">Stop Starting<br><span class="accent" style="font-size:44px">Over Every</span><br>Monday</h2>
  <p class="tagline" style="left:27px;top:212px;font-size:19px">Stay Consistent<br>with <span class="accent">MB in Your</span><br><span class="accent">Pocket!</span></p>
</section>

<section class="card col-r row-1">
  <div class="shape ring" style="left:108px;top:360px;width:500px;height:500px"></div>
  <div class="photo" role="img" aria-label="Coach hugging a smiling client" style="left:128px;top:270px;width:520px;height:520px;border-radius:50% 0 0 0"></div>
  <h2 class="headline" style="left:22px;top:34px;font-size:48px">You don't need<br>more willpower.<br><span class="accent">You need<br>more support</span></h2>
  <p class="tagline" style="left:22px;top:264px;font-size:21px">Stay Consistent<br>with <span class="accent">MB in Your</span><br><span class="accent">Pocket!</span></p>
</section>

<section class="card col-l row-2">
  <div class="shape ring" style="left:-150px;top:205px;width:470px;height:470px"></div>
  <div class="photo" role="img" aria-label="Coach standing with a laughing client at an event" style="left:-175px;top:205px;width:470px;height:470px"></div>
  <h2 class="headline center" style="left:0;width:431px;top:38px;font-size:46px">Built for women<br><span class="accent">who are tired of</span><br>doing this alone</h2>
  <p class="tagline right" style="right:34px;top:210px;font-size:20px">Stay Consistent<br>with <span class="accent">MB in Your</span><br><span class="accent">Pocket!</span></p>
</section>

<section class="card col-r row-2">
  <div class="shape ring" style="left:-170px;top:198px;width:454px;height:454px"></div>
  <div class="photo" role="img" aria-label="Coach smiling beside a pool table" style="left:-190px;top:198px;width:454px;height:454px"></div>
  <h2 class="headline center" style="left:0;width:431px;top:30px;font-size:42px">When Motivation<br><span style="font-size:58px">Fades,</span><br><span class="accent" style="font-size:46px">MB Checks In</span></h2>
  <p class="tagline center" style="left:268px;width:150px;top:216px;font-size:22px;line-height:1.3">Stay<br>Consistent<br>with<br><span class="accent">MB in Your<br>Pocket!</span></p>
</section>

<section class="card col-l row-3">
  <div class="shape ring" style="left:116px;top:-160px;width:345px;height:345px"></div>
  <div class="photo" role="img" aria-label="Coach hugging a smiling client" style="left:140px;top:-160px;width:345px;height:345px"></div>
  <h2 class="headline" style="left:30px;top:198px;font-size:52px">The<br>Support<br><span class="accent">System You've<br>Been Missing</span></h2>
  <p class="tagline" style="left:30px;top:440px;font-size:22px">Stay Consistent with<br><span class="accent">MB in Your Pocket!</span></p>
</section>

<section class="card col-r row-3">
  <div class="shape ring" style="left:130px;top:-290px;width:460px;height:460px"></div>
  <div class="shape soft" style="left:162px;top:-280px;width:450px;height:450px"></div>
  <div class="cutout" role="img" aria-label="Coach smiling in black lace top, hand on hip" style="left:262px;top:36px;width:169px;height:502px"></div>
  <h2 class="headline" style="left:24px;top:164px;font-size:38px;line-height:1.18">Support<br>When<br><span class="accent">Motivation<br>Disappears</span></h2>
  <p class="tagline" style="left:24px;top:400px;font-size:22px">Stay Consistent<br>with <span class="accent">MB in Your</span><br><span class="accent">Pocket!</span></p>
</section>

<section class="card col-l row-4">
  <div class="shape ring" style="left:-130px;top:-170px;width:440px;height:440px"></div>
  <div class="photo" role="img" aria-label="Coach smiling in black lace top" style="left:-155px;top:-170px;width:440px;height:440px"></div>
  <h2 class="headline right" style="right:30px;top:224px;font-size:52px;line-height:1.1">What<br>if <span class="accent">MB Checked</span><br>in Every Day?</h2>
  <p class="tagline right" style="right:30px;top:412px;font-size:24px">Stay Consistent with<br><span class="accent">MB in Your Pocket!</span></p>
</section>

<section class="card col-r row-4">
  <div class="shape ring" style="left:-120px;top:-170px;width:430px;height:430px"></div>
  <div class="photo" role="img" aria-label="Coach standing with a laughing client at an event" style="left:-150px;top:-170px;width:430px;height:430px"></div>
  <h2 class="headline right" style="right:30px;top:178px;font-size:50px;line-height:1.12">The<br>Missing<br>Piece <span class="accent">Isn't</span><br><span class="accent">Another Diet</span></h2>
  <p class="tagline right" style="right:30px;top:412px;font-size:24px">Stay Consistent with<br><span class="accent">MB in Your Pocket!</span></p>
</section>

<section class="card col-l row-5">
  <div class="shape ring" style="left:245px;top:300px;width:360px;height:360px"></div>
  <div class="shape white" style="left:205px;top:330px;width:300px;height:300px"></div>
  <div class="shape ring" style="left:272px;top:300px;width:360px;height:360px"></div>
  <div class="cutout" role="img" aria-label="Coach smiling in black lace top, hand on hip" style="left:310px;top:300px;width:121px;height:238px"></div>
  <h2 class="headline" style="left:27px;top:34px;font-size:54px;line-height:1.05">Eat the food<br>you love.<br><span class="accent">Stay<br>accountable<br>every day.</span></h2>
  <p class="tagline" style="left:27px;top:380px;font-size:21px">Stay Consistent<br>with <span class="accent">MB in Your</span><br><span class="accent">Pocket!</span></p>
</section>

<section class="card col-r row-5">
  <div class="shape ring" style="left:335px;top:30px;width:240px;height:240px"></div>
  <div class="shape ring" style="left:205px;top:410px;width:360px;height:360px"></div>
  <div class="photo" role="img" aria-label="Coach hugging a smiling client" style="left:232px;top:185px;width:285px;height:285px"></div>
  <h2 class="headline" style="left:26px;top:40px;font-size:56px;line-height:0.99">One<br>Bad Meal<br><span class="accent">Doesn't<br>Mean<br>You<br>Failed</span></h2>
  <p class="tagline" style="left:26px;top:416px;font-size:21px">Stay Consistent<br>with <span class="accent">MB in Your</span><br><span class="accent">Pocket!</span></p>
</section>

</main>
</body>
</html>
```